Tailbrook Website Design

Need a website for a Dog Grooiming business. Please make it simular to these:

https://www.furvanto.com
https://haulnorix.com
https://meadowpetrin.com
https://www.drivelumo.com/search/

```html
<!DOCTYPE html>
<html lang="en">
<head>
<meta charset="utf-8">
<title>Tailbrook — Dog Grooming</title>
<link rel="stylesheet" href="https://fonts.googleapis.com/css2?family=Inter:wght@300;400;500&family=Montserrat:wght@600;700&display=swap">
<style>
:root{
  --yellow:#fdb813;
  --ink:#2b0608;
  --ink-soft:#4a2a2b;
  --footer:#2b0000;
  --footer-link:#b9aaaa;
  --sky:#c3d5ef;
  --white:#ffffff;
}
*{box-sizing:border-box;margin:0;padding:0}
html,body{width:1200px;height:2398px;overflow:hidden;background:var(--white)}
body{position:relative;font-family:"Inter",sans-serif;color:var(--ink)}
a{text-decoration:none;color:inherit}
.abs{position:absolute}

/* nav */
.site-nav{position:absolute;left:0;top:0;width:1200px;height:64px;background:var(--yellow);z-index:3}
.site-nav a{position:absolute;top:24px;font-size:15px;font-weight:300;color:var(--ink);transform:translateX(-50%);white-space:nowrap}
.brand-badge{position:absolute;left:543px;top:0;width:102px;height:106px;border-radius:0 0 51px 51px;background:var(--yellow);z-index:4;display:flex;align-items:flex-end;justify-content:center;padding-bottom:22px}
.brand-badge span{font-family:"Montserrat",sans-serif;font-weight:700;font-size:14px;color:var(--ink);letter-spacing:.3px}

/* hero */
.hero-photo{left:0;top:64px;width:1200px;height:572px;
  background:
    radial-gradient(ellipse 300px 330px at 370px 250px,#d9b98c 0%,rgba(217,185,140,.85) 45%,rgba(217,185,140,0) 100%),
    radial-gradient(ellipse 420px 220px at 980px 360px,#f0b9c6 0%,rgba(240,185,198,.8) 50%,rgba(240,185,198,0) 100%),
    radial-gradient(ellipse 260px 160px at 300px 400px,#f3d3d6 0%,rgba(243,211,214,0) 100%),
    linear-gradient(180deg,#d9c7b1 0%,#e6d7cc 40%,#bdb7b4 75%,#a9a5a3 100%)}
.hero-title{left:592px;top:168px;font-size:46px;line-height:56px;font-weight:400;color:var(--ink);letter-spacing:-.3px}
.hero-text{left:592px;top:279px;width:420px;font-size:17.5px;line-height:22.5px;font-weight:400;color:var(--ink)}
.btn-primary{left:589px;top:361px;width:168px;height:45px;background:var(--yellow);border-radius:2px;display:flex;align-items:center;justify-content:center;font-size:16px;font-weight:500;color:var(--ink)}

/* offer */
.section-title{left:0;width:1200px;text-align:center;font-size:36px;font-weight:300;color:var(--ink)}
.section-sub{left:0;width:1200px;text-align:center;font-size:15px;line-height:20px;font-weight:300;color:var(--ink-soft)}
.service{text-align:center;transform:translateX(-50%)}
.service-art{width:130px;height:122px;margin:0 auto;background:linear-gradient(180deg,#f4f4f4,#e6e6e6);border-radius:6px}
.service h3{margin-top:17px;font-size:16px;font-weight:400}
.service p{margin:3px auto 0;font-size:13px;line-height:17px;font-weight:300}

/* story */
.story-band{left:0;top:1019px;width:1200px;height:319px;background:var(--sky)}
.story-photo{left:230px;top:1019px;width:370px;height:319px;background:radial-gradient(ellipse at 45% 60%,#efe6db 0%,#d9cbbb 45%,rgba(195,213,239,0) 75%)}
.story-brand{left:700px;top:1078px;font-family:"Montserrat",sans-serif;font-weight:700;font-size:34px;color:var(--ink);letter-spacing:.5px}
.story-kicker{left:703px;top:1133px;font-size:19px;font-weight:400}
.story-text{left:703px;top:1163px;width:298px;font-size:13px;line-height:17px;font-weight:300}

/* testimonials */
.testimonials{left:0;top:1338px;width:1200px;height:210px}
.avatar{width:92px;height:92px;border-radius:50%;border:2px solid var(--ink);background:linear-gradient(135deg,#c9b9a8,#8d6e5a)}
.quote{font-size:13px;line-height:17px;font-weight:300;color:var(--ink)}
.handle{font-size:13px;font-weight:400;color:var(--ink);text-align:right}

/* pricing */
.plan{width:240px;text-align:center;transform:translateX(-50%)}
.plan-art{width:150px;height:150px;margin:0 auto;background:linear-gradient(180deg,#f3f3f3,#e3e3e3);border-radius:6px}
.plan-price{margin-top:26px;font-size:36px;font-weight:400;line-height:40px}
.plan-desc{font-size:14px;font-weight:300;margin-top:2px}
.btn-choose{display:block;width:131px;height:28px;margin:22px auto 0;background:var(--yellow);border-radius:2px;font-size:14px;font-weight:300;line-height:28px;color:var(--ink)}

/* footer */
.site-footer{left:0;top:2023px;width:1200px;height:375px;background:var(--footer)}
.footer-brand{left:0;top:2140px;width:1200px;text-align:center;font-family:"Montserrat",sans-serif;font-weight:600;font-size:28px;color:var(--yellow);letter-spacing:1px}
.footer-mark{left:577px;top:2080px;width:46px;height:46px;background:var(--yellow);border-radius:50%}
.social{top:2245px;width:26px;height:26px;border-radius:50%;background:var(--white)}
.footer-nav a{position:absolute;top:2300px;transform:translateX(-50%);font-size:16px;font-weight:400;color:var(--footer-link);white-space:nowrap}
.footer-nav a.is-active{color:var(--white)}
</style>
</head>
<body>

<nav class="site-nav">
  <a href="#" style="left:217px">Home</a>
  <a href="#" style="left:321px">About</a>
  <a href="#" style="left:452px">Dog Day Care</a>
  <a href="#" style="left:707px">Grooming</a>
  <a href="#" style="left:845px">Testimonial</a>
  <a href="#" style="left:972px">Contact</a>
</nav>
<div class="brand-badge"><span>TAILBROOK</span></div>

<header>
  <div class="abs hero-photo" role="img" aria-label="Photo of a small long-haired terrier in a pink robe and slippers on a grey rug, beside folded pink towels, a brush and bows"></div>
  <h1 class="abs hero-title">Make your dog feel<br>like a top dog</h1>
  <p class="abs hero-text">We all know how good we feel after a bath or shower and a visit to the hair salon – your pet is no different</p>
  <a class="abs btn-primary" href="#">GET STARTED</a>
</header>

<section>
  <h2 class="abs section-title" style="top:668px">What we offer</h2>
  <p class="abs section-sub" style="top:716px">All dogs are styled to breed standard unless you request otherwise.<br>We will never shave down your dog unless previously discussed</p>

  <div class="abs service" style="left:313px;top:773px;width:250px">
    <div class="service-art" role="img" aria-label="Line drawing of a dog resting in a doghouse"></div>
    <h3>Boarding Dog</h3>
    <p style="width:250px">Just like you, we want your pet's boarding experience to be as positive as possible</p>
  </div>
  <div class="abs service" style="left:608px;top:773px;width:210px">
    <div class="service-art" role="img" aria-label="Line drawing of a sitting dog being held"></div>
    <h3>Sitting Dog</h3>
    <p style="width:205px">Pet sitting Services Style of Your Preference Removal of Ear Canal Hair</p>
  </div>
  <div class="abs service" style="left:868px;top:773px;width:220px">
    <div class="service-art" role="img" aria-label="Line drawing of a dog being bathed in a tub"></div>
    <h3>Grooming Dog</h3>
    <p style="width:218px">All bath Services 3 Step De-SheddingProcessTrim and Thin Around</p>
  </div>
</section>

<section>
  <div class="abs story-band"></div>
  <div class="abs story-photo" role="img" aria-label="Photo of a white retriever wearing a reindeer antler headband"></div>
  <h2 class="abs story-brand">TAILBROOK</h2>
  <h3 class="abs story-kicker">OUR STORY</h3>
  <p class="abs story-text">Tailbrook was founded on two basic principals; do what you promise with complete transparency and do your bEST work everyday. So many grooming salons are dark and dirty with cranky, stressed out animals and people. We strive to be different. We are just like a human hair salon</p>
</section>

<section>
  <svg class="abs testimonials" width="1200" height="210" viewBox="0 0 1200 210" aria-hidden="true">
    <polygon points="0,0 1200,0 1200,209 0,167" fill="#fdb813"/>
  </svg>
  <div class="abs avatar" style="left:197px;top:1362px" role="img" aria-label="Photo of two small white dogs"></div>
  <p class="abs quote" style="left:308px;top:1381px;width:245px">I am recommending Miss Nora Fenwick as a dog groomer. Miss Fenwick has groomed my dog Pete for about 2 years.</p>
  <p class="abs handle" style="left:396px;top:1472px;width:200px">@Marla_PupFan</p>

  <div class="abs avatar" style="left:648px;top:1362px" role="img" aria-label="Photo of a chihuahua wearing a red beret"></div>
  <p class="abs quote" style="left:757px;top:1381px;width:245px">Nora is so wonderful with dogs! Bugsy loves when Nora grooms him :) She is so calm and talented.</p>
  <p class="abs handle" style="left:780px;top:1472px;width:220px">@Benny_andRoverPal</p>
</section>

<section>
  <h2 class="abs section-title" style="top:1570px">Our Pricing</h2>
  <p class="abs section-sub" style="top:1615px;left:-16px">Find the perfect price for your pets</p>

  <div class="abs plan" style="left:334px;top:1688px">
    <div class="plan-art" role="img" aria-label="Pencil drawing of a small terrier"></div>
    <div class="plan-price">$70</div>
    <div class="plan-desc">Small Dogs age 3-8 months old</div>
    <a class="btn-choose" href="#">Choose</a>
  </div>
  <div class="abs plan" style="left:606px;top:1688px">
    <div class="plan-art" role="img" aria-label="Pencil drawing of a medium crested dog"></div>
    <div class="plan-price">$90</div>
    <div class="plan-desc">Medium Dogs age 1-3 Years old</div>
    <a class="btn-choose" href="#">Choose</a>
  </div>
  <div class="abs plan" style="left:887px;top:1688px">
    <div class="plan-art" role="img" aria-label="Pencil drawing of a large wrinkled dog"></div>
    <div class="plan-price">$100</div>
    <div class="plan-desc">Large Dogs age 4-10 Years old</div>
    <a class="btn-choose" href="#">Choose</a>
  </div>
</section>

<footer>
  <div class="abs site-footer"></div>
  <div class="abs footer-mark"></div>
  <div class="abs footer-brand">TAILBROOK</div>
  <a class="abs social" style="left:489px" href="#" aria-label="Social profile 1"></a>
  <a class="abs social" style="left:552px" href="#" aria-label="Social profile 2"></a>
  <a class="abs social" style="left:616px" href="#" aria-label="Social profile 3"></a>
  <a class="abs social" style="left:679px" href="#" aria-label="Social profile 4"></a>
  <nav class="footer-nav">
    <a class="is-active" href="#" style="left:293px">Home</a>
    <a href="#" style="left:385px">About</a>
    <a href="#" style="left:514px">Doggy day care</a>
    <a href="#" style="left:666px">Grooming</a>
    <a href="#" style="left:795px">Testimonials</a>
    <a href="#" style="left:914px">Contact</a>
  </nav>
</footer>

</body>
</html>
```